Plakat für Hersteller von maßgefertigten Tischunikaten aus Massivholz
Zielgruppe
Wir sind einen Firma die sich auf die Fertigung von maßgefertigten Tischunikaten aus Massivholz spezialisiert hat. Unsere Zielgruppe sind Design affine Leute, im Alter von 35-55 Jahren
Aufgabenstellung
Wir benötigen das Design für eine Messewand mit den Maßen 443X227 cm. 5 Zentimeter rundlaufen dürfen keine Elemente mehr platziert werden. Die Messewand steht im Hintergrund von unserem Stand bei verschiedenen Designmessen
Infos die auf die Messewand müssen: Logo, Tischmanufaktur aus Stuttgart, Maßgefertigte Tischunikate (Bei der Formulierung bin ich flexibel, ihr könnt bspw. auch nur Stichworte benutzen, aber Stuttgart und maßgefertigt ist wichtig).
Die Messewand soll sehr minimalistisch gestaltet sein, bei der letzten Messewand hatten wir ein Foto von einem Tisch im Hintergrund und das sah merkwürdig aus.

```html
<!DOCTYPE html>
<html lang="de">
<head>
<meta charset="utf-8">
<title>Lindqvist Manufaktur – Messewand</title>
<link rel="stylesheet" href="https://fonts.googleapis.com/css2?family=Roboto+Slab:wght@300&family=Source+Sans+3:wght@700&family=Open+Sans:wght@400&display=swap">
<style>
  :root {
    --page: #ededed;
    --wall-black: #0b0b0b;
    --wall-glow: #2a2a2a;
    --ink-light: #f4f1ee;
    --band-white: #ffffff;
    --band-ink: #1a1a1a;
    --highlight: #5b5b5b;
    --grain-dark: #1c1a19;
    --grain-light: #b9b0a9;
  }
  * { margin: 0; padding: 0; box-sizing: border-box; }
  html, body { width: 1200px; height: 800px; overflow: hidden; background: var(--page); }

  .trade-wall {
    position: absolute;
    left: 40px; top: 113px;
    width: 1120px; height: 574px;
    overflow: hidden;
    box-shadow: 0 10px 30px rgba(0,0,0,0.18);
  }

  .wall-header {
    position: absolute; inset: 0 0 auto 0;
    height: 287px;
    background:
      radial-gradient(ellipse 220px 90px at 32% 32%, rgba(255,255,255,0.14), transparent 70%),
      radial-gradient(ellipse 240px 100px at 80% 45%, rgba(255,255,255,0.10), transparent 70%),
      linear-gradient(180deg, var(--wall-glow) 0%, var(--wall-black) 55%, var(--wall-black) 100%);
  }

  .brand {
    position: absolute; left: 36px; top: 60px;
    display: flex; align-items: center; gap: 22px;
  }
  .brand-mark {
    width: 88px; height: 88px;
    border: 5px solid var(--ink-light);
    border-radius: 50%;
  }
  .brand-name {
    font-family: "Roboto Slab", serif;
    font-weight: 300;
    font-size: 23px;
    line-height: 1.38;
    color: var(--ink-light);
  }

  .headline {
    position: absolute; left: 560px; top: 68px;
    font-family: "Source Sans 3", sans-serif;
    font-weight: 700;
    font-size: 43px;
    line-height: 1.3;
    color: var(--ink-light);
    letter-spacing: 0.2px;
  }
  .headline .place {
    background: var(--highlight);
    padding: 0 6px 0 4px;
  }

  .url-band {
    position: absolute; left: 0; right: 0; top: 287px;
    height: 42px;
    background: var(--band-white);
    overflow: hidden;
    white-space: nowrap;
    font-family: "Open Sans", sans-serif;
    font-size: 21px;
    line-height: 42px;
    color: var(--band-ink);
  }
  .url-band .url {
    position: absolute; top: 0;
  }

  .grain-field {
    position: absolute; left: 0; right: 0; top: 329px; bottom: 0;
    background:
      repeating-linear-gradient(95deg, var(--grain-dark) 0 14px, #4a4542 14px 17px, var(--grain-dark) 17px 30px),
      var(--grain-dark);
    opacity: 0.96;
  }
</style>
</head>
<body>
  <section class="trade-wall">
    <div class="wall-header">
      <div class="brand">
        <div class="brand-mark"></div>
        <div class="brand-name">Lindqvist<br>Manufaktur</div>
      </div>
      <h1 class="headline">Ihr Tisch. Ihr Unikat.<br>Maßgefertigt in <span class="place">Stuttgart.</span></h1>
    </div>

    <div class="url-band">
      <span class="url" style="left:-30px">www. lindqvist-manufaktur.de</span>
      <span class="url" style="left:302px">www. lindqvist-manufaktur.de</span>
      <span class="url" style="left:680px">www. lindqvist-manufaktur.de</span>
      <span class="url" style="left:1056px">www. lindqvist-manufaktur.de</span>
    </div>

    <div class="grain-field" role="img" aria-label="Grafisches Holzmaserungsmuster mit Astlöchern in Hellbeige auf Schwarz"></div>
  </section>
</body>
</html>
```